Kestriva Business Card Design - double sided -plumbing local plumbing company

We have a Plumbing company where the design was create through Makerhive. We would now like a business card designed as well. We want it to be in the colour version of the logo.

Details below for the card.

Phone Number: 0468 215 374
Email: info@kestrivapipeworks.com.au
Website: https://kestrivapipeworks.com.au
We really want a sophisticated design that stand out from the other- informative and timeless.

Target Market(s)

local Canberra market

Industry/Entity Type

Plumbing, gas fitting, hot water

Contact Information for Business Card

Phone number, email, logo and "Supplying all your heating, cooling and hot water needs"

Requirements
Must have
• bust be colourful, must also be though about it being printed on a magnet. must Flo with the logo - I dont want the logo and information chucked onto a white canvas I would prefer it to be smooth and look purposeful

```html
<!DOCTYPE html>
<html lang="en">
<head>
<meta charset="utf-8">
<title>Kestriva Business Card</title>
<link rel="stylesheet" href="https://fonts.googleapis.com/css2?family=Montserrat:wght@700&family=Open+Sans:wght@400;600&display=swap">
<style>
  :root {
    --stage: #232323;
    --card: #1c1c1c;
    --blue: #02acee;
    --orange: #fbb040;
    --white: #ffffff;
    --ghost: #1f2526;
  }
  * { box-sizing: border-box; margin: 0; padding: 0; }
  html, body { width: 1200px; height: 711px; overflow: hidden; background: var(--stage); }
  .stage { position: relative; width: 1200px; height: 711px; }
  .card {
    position: absolute; top: 196px; width: 560px; height: 320px;
    background: var(--card); overflow: hidden;
    font-family: "Open Sans", Arial, sans-serif; color: var(--white);
  }
  .card--back { left: 27px; }
  .card--front { left: 613px; }
  .card svg.bands { position: absolute; inset: 0; }
  .back-web {
    position: absolute; right: 34px; bottom: 14px;
    font-size: 12px; font-weight: 600; color: var(--white);
  }
  .brand {
    position: absolute; left: 30px; top: 40px;
    font-family: "Montserrat", Arial, sans-serif; font-weight: 700;
    font-size: 40px; letter-spacing: 1px; color: var(--blue);
  }
  .person { position: absolute; right: 40px; top: 74px; text-align: right; }
  .person__name {
    font-family: "Montserrat", Arial, sans-serif; font-weight: 700;
    font-size: 25px; color: var(--blue); line-height: 1;
  }
  .person__name span { color: var(--orange); }
  .person__role { font-size: 13px; font-weight: 600; margin-top: 4px; }
  .tagline {
    position: absolute; right: 40px; top: 180px; text-align: right;
    font-size: 12px; line-height: 1.4;
  }
  .contacts { position: absolute; left: 34px; top: 210px; list-style: none; }
  .contacts li {
    display: flex; align-items: center; gap: 8px;
    font-size: 13px; line-height: 1.55;
  }
  .contacts svg { width: 13px; height: 13px; flex: none; }
</style>
</head>
<body>
<main class="stage">

  <section class="card card--back" aria-label="Card back">
    <svg class="bands" viewBox="0 0 560 320" aria-hidden="true">
      <circle cx="420" cy="120" r="96" fill="var(--blue)"/>
      <polygon points="330,280 560,280 560,320 312,320" fill="var(--orange)"/>
      <polygon points="0,306 305,306 300,320 0,320" fill="var(--blue)"/>
    </svg>
    <p class="back-web">www.kestrivapipeworks.com.au</p>
  </section>

  <section class="card card--front" aria-label="Card front">
    <svg class="bands" viewBox="0 0 560 320" aria-hidden="true">
      <circle cx="450" cy="110" r="90" fill="var(--ghost)"/>
      <rect x="524" y="66" width="20" height="44" fill="var(--orange)"/>
      <line x1="30" y1="160" x2="330" y2="160" stroke="var(--blue)" stroke-width="1.5"/>
      <polygon points="0,300 350,300 343,320 0,320" fill="var(--orange)"/>
      <polygon points="356,300 560,300 560,320 349,320" fill="var(--blue)"/>
    </svg>

    <h1 class="brand">KESTRIVA</h1>

    <div class="person">
      <p class="person__name">Tomas <span>Veldren</span></p>
      <p class="person__role">Managing Director</p>
    </div>

    <p class="tagline">Supplying all your heating,<br>cooling and hot water needs</p>

    <ul class="contacts">
      <li>
        <svg viewBox="0 0 16 16" aria-hidden="true"><path fill="var(--orange)" d="M3.6 1.2l2.3 2.6-1.3 1.8c.9 2 2.5 3.6 4.5 4.6l1.8-1.3 2.6 2.3-1.2 2.2C7 13.4 2.6 9 1.4 3.1z"/></svg>
        <span>0468 215 374</span>
      </li>
      <li>
        <svg viewBox="0 0 16 16" aria-hidden="true"><circle cx="8" cy="8" r="6.5" fill="none" stroke="var(--orange)" stroke-width="1.6"/><path d="M1.5 8h13M8 1.5c-3 3.5-3 9.5 0 13M8 1.5c3 3.5 3 9.5 0 13" fill="none" stroke="var(--orange)" stroke-width="1.2"/></svg>
        <span>www.kestrivapipeworks.com.au</span>
      </li>
      <li>
        <svg viewBox="0 0 16 16" aria-hidden="true"><rect x="1" y="3" width="14" height="10" fill="var(--orange)"/><path d="M1 3l7 6 7-6" fill="none" stroke="var(--card)" stroke-width="1.3"/></svg>
        <span>info@kestrivapipeworks.com.au</span>
      </li>
    </ul>
  </section>

</main>
</body>
</html>
```